quorvaAgency Business Card Design Project

We need a business card design for quorvaAgency. quorvaAgency is an underwriting agency. Underwriting agencies act on behalf of insurers, to underwrite insurance. We will be operating in specialised classes of insurance initially and looking to expand from there. We would like to see designs that incorporate our logo colours as well as a contrasting stand out colour - also we'd like the logo itself to be embossed on the card.

Industry/Entity Type

Insurance

Requirements
Must have
• Logo on front
Nice to have
• Logo solely featured on back of card
Should not have
• Please do not use comic cans font :)

```html
<!DOCTYPE html>
<html lang="en">
<head>
<meta charset="utf-8">
<title>quorvaAgency Business Card</title>
<link rel="stylesheet" href="https://fonts.googleapis.com/css2?family=Arimo:wght@400;700&display=swap">
<style>
  :root {
    --brand-blue: #1d5fa8;
    --brand-blue-deep: #0a4f92;
    --brand-blue-light: #2b78c4;
    --ink: #3a3a3c;
    --ink-soft: #555558;
    --band-dark: #404042;
    --card-edge: #b9b9bb;
    --page: #ffffff;
  }
  * { box-sizing: border-box; margin: 0; padding: 0; }
  html, body {
    width: 1200px; height: 900px; overflow: hidden;
    background: var(--page);
    font-family: "Arimo", Arial, sans-serif;
  }
  .canvas { position: relative; width: 1200px; height: 900px; }

  .card {
    position: absolute; top: 279px;
    width: 525px; height: 326px;
    border-radius: 12px; overflow: hidden;
  }

  /* Front */
  .card-front {
    left: 40px;
    border: 1px solid var(--card-edge);
    background: linear-gradient(180deg, #ffffff 0%, #f4f5f6 70%, #eceded 100%);
  }
  .side-tab {
    position: absolute; top: 69px; width: 16px; height: 187px;
    background: var(--brand-blue);
  }
  .side-tab.left { left: 0; border-radius: 0 6px 6px 0; }
  .side-tab.right { right: 0; border-radius: 6px 0 0 6px; }

  .front-mark {
    position: absolute; left: 115px; top: 88px;
    width: 80px; height: 80px; border-radius: 50%;
    background: var(--brand-blue);
  }
  .front-name {
    position: absolute; left: 38px; top: 172px;
    width: 240px; text-align: center;
    font-size: 31px; font-weight: 700; color: var(--brand-blue);
    letter-spacing: -0.5px;
  }

  .person { position: absolute; left: 298px; top: 97px; color: var(--ink); }
  .person-name { font-size: 16px; font-weight: 700; line-height: 19px; }
  .person-role { font-size: 15px; font-weight: 700; line-height: 19px; }

  .contacts { position: absolute; left: 301px; top: 164px; list-style: none; }
  .contacts li {
    display: flex; align-items: center; height: 16.5px;
    font-size: 11px; color: var(--ink-soft);
  }
  .contacts li:nth-child(2) { margin-bottom: 1px; }
  .contacts svg { width: 11px; height: 11px; margin-right: 14px; fill: var(--ink); }

  .front-web {
    position: absolute; left: 0; right: 0; top: 294px; text-align: center;
    font-size: 11px; letter-spacing: 4.5px; color: var(--ink);
  }
  .front-rule {
    position: absolute; left: 70px; right: 70px; height: 1px;
    background: linear-gradient(90deg, transparent, #c9c9cb, transparent);
  }

  /* Back */
  .card-back { left: 628px; background: var(--band-dark); }
  .back-field {
    position: absolute; left: 0; top: 0; width: 100%; height: 268px;
    background: radial-gradient(ellipse at 50% 45%, var(--brand-blue-light) 0%, var(--brand-blue-deep) 75%);
    border-bottom: 3px solid #d6dde6;
  }
  .back-mark {
    position: absolute; left: 216px; top: 68px;
    width: 96px; height: 96px; border-radius: 50%;
    background: #ffffff;
  }
  .back-name {
    position: absolute; left: 0; right: 0; top: 168px; text-align: center;
    font-size: 46px; font-weight: 700; color: #ffffff; letter-spacing: -0.5px;
  }
  .back-web {
    position: absolute; left: 0; right: 0; top: 284px; text-align: center;
    font-size: 14px; letter-spacing: 3px; color: #ffffff;
  }
</style>
</head>
<body>
<main class="canvas">
  <section class="card card-front" aria-label="Card front">
    <div class="side-tab left"></div>
    <div class="side-tab right"></div>
    <div class="front-mark"></div>
    <div class="front-name">quorvaAgency</div>
    <div class="person">
      <p class="person-name">Your Name</p>
      <p class="person-role">Current Postion</p>
    </div>
    <ul class="contacts">
      <li><svg viewBox="0 0 12 12"><path d="M2.5 1l2 2.2-1 1.3c.7 1.5 1.8 2.6 3.2 3.3l1.3-1 2.2 2-1.2 1.8C5 10.4 1.6 7 .9 2.2z"/></svg>012 345 6789</li>
      <li><svg viewBox="0 0 12 12"><rect x="3.5" y="1" width="5" height="10" rx="1"/></svg>012 345 6789</li>
      <li><svg viewBox="0 0 12 12"><rect x="1" y="3" width="10" height="6" rx="3"/></svg>yournick@chatline.com</li>
      <li><svg viewBox="0 0 12 12"><rect x="1" y="2.5" width="10" height="7"/></svg>yourmail@quorvaagency.com</li>
    </ul>
    <div class="front-rule" style="top:290px"></div>
    <div class="front-web">www.yourwebsite.com</div>
    <div class="front-rule" style="top:311px"></div>
  </section>

  <section class="card card-back" aria-label="Card back">
    <div class="back-field">
      <div class="back-mark"></div>
      <div class="back-name">quorvaAgency</div>
    </div>
    <div class="back-web">www.yourwebsite.com</div>
  </section>
</main>
</body>
</html>
```